Design for mobile and web app for sweepstakes.

We need the design for a mobile app (planned to be build with jquery mobile) and web app (mobile first, we will use same look and feel as mobile just with displaying more info at once).

The following pages must be included:
- Userregistration/Login (Reg via Email, Chatnook-Reg)

- List of available sweepstakes (including some icons: a video icon, a "like button" type icon, a "provide some info" type of icon) this should be on the side in wep app but in mobile app its a list. possible is also a mobile display where users can swipe back and forth through it.

- single sweepstake detailview . should present a single sweepstake and give users the opportunity to participate with a button.

user settings. (doesnt not have to include a lot of fields we will at ourself. should contain some datepicker (birthday), some on/off switch (receive newsletters) some textfield in order for us to have a feel.

We have included the following files:
- prizewell_logo_final01.png:
this is our logo which should be used and also the look and feel must fit with the logo.

- prizewell_logo_final06.png:
this is the app-icon

this is a simple mockup for a registration page. the design doesnt have to contain all fields we will do that ourselfes starting from your handover, but should represent a common registration page with some fields

this is just a mockup for a possible design. not that it does use our old logo. This again is not binding is just to get a feel for what we are looking for. A list of sweepstakes and a detailspage for the sweepstake for users to participate in it.

Target Market(s)

German speaking users, Austria, Germany, Switzerland
The app is adressing a wide crowd of users who are interested in participating in sweepstakes.

Industry/Entity Type

Build

Number of Pages Required

4 page

Font styles to use
Sans Serif

Requirements
Must have
• - jquery and jquery mobile
• - html5 (preferable bootstrap-based)
• - css3
• - description on used fonts and colors. fonts must be free to use and publicly available for anyone to use.
• - all buttons should be css

```html
<!DOCTYPE html>
<html lang="de">
<head>
<meta charset="utf-8">
<title>prizewell – Gewinnspiele</title>
<link rel="stylesheet" href="https://fonts.googleapis.com/css2?family=Quicksand:wght@400;500;600;700&display=swap">
<style>
  :root {
    --green: #6ba433;
    --green-dark: #43611f;
    --green-soft: #c9ddc1;
    --status-green: #93c08d;
    --band-from: #8cb888;
    --band-to: #c1dcb9;
    --blue: #1f7fb5;
    --text: #3a3a3a;
    --white: #ffffff;
    --input-bg: #fff8f8;
    --rule: #d9d9d9;
    --teal: #1bb69c;
    --orange: #f7a531;
    --navy: #1e3645;
  }
  * { box-sizing: border-box; margin: 0; padding: 0; }
  html, body { width: 676px; height: 1200px; overflow: hidden; background: var(--white); }
  body { font-family: "Quicksand", sans-serif; color: var(--text); }
  .screen { position: relative; width: 676px; height: 1200px; overflow: hidden; background: var(--white); }

  .status-bar {
    position: absolute; left: 0; top: 0; width: 676px; height: 42px;
    background: var(--status-green); color: var(--white);
    font-family: "Helvetica Neue", Arial, sans-serif; font-size: 22px;
    display: flex; align-items: center; justify-content: space-between; padding: 0 14px;
  }
  .status-bar .carrier { display: flex; align-items: center; gap: 8px; }
  .status-bar .time { position: absolute; left: 0; right: 0; text-align: center; pointer-events: none; }
  .status-bar .battery { display: flex; align-items: center; gap: 8px; }

  .app-header {
    position: absolute; left: 0; top: 42px; width: 676px; height: 135px;
    background: linear-gradient(#ffffff, #f3f3f3);
  }
  .app-header .back { position: absolute; left: 20px; top: 38px; }
  .app-header .menu { position: absolute; left: 598px; top: 42px; }
  .brand {
    position: absolute; left: 0; right: 0; top: 42px; text-align: center;
    font-size: 44px; font-weight: 700; color: var(--green); letter-spacing: -0.5px;
  }

  .search-band {
    position: absolute; left: 0; top: 177px; width: 676px; height: 124px;
    background: linear-gradient(100deg, var(--band-from), var(--band-to));
  }
  .search-field {
    position: absolute; left: 17px; top: 19px; width: 644px; height: 87px;
    background: var(--input-bg); border-radius: 3px;
    display: flex; align-items: center; padding: 0 22px;
  }
  .search-field .placeholder { flex: 1; font-size: 20px; color: #e6dada; }

  .sweepstake {
    position: absolute; left: 0; width: 676px; height: 154px;
    background: var(--white); border-bottom: 3px solid var(--rule);
  }
  .sweepstake .thumb {
    position: absolute; left: 11px; top: 12px; width: 133px; height: 133px; border-radius: 50%;
  }
  .thumb.teal { background: var(--teal); }
  .thumb.orange { background: var(--orange); }
  .thumb.navy { background: var(--navy); }
  .sweepstake .title {
    position: absolute; left: 160px; top: 24px; font-size: 25px; font-weight: 700; color: var(--green);
  }
  .sweepstake .teaser {
    position: absolute; left: 160px; top: 62px; font-size: 21px; font-weight: 500; color: var(--text);
  }
  .sweepstake .deadline {
    position: absolute; left: 160px; top: 102px; font-size: 21px; font-weight: 700; color: var(--blue);
    display: flex; gap: 46px;
  }
  .sweepstake .reveal { position: absolute; left: 633px; top: 52px; }
  .sweepstake .actions {
    position: absolute; left: 510px; top: 0; width: 166px; height: 151px;
    background: var(--green); display: flex; align-items: center; justify-content: center; gap: 8px;
  }

  .tab-bar { position: absolute; left: 0; top: 1085px; width: 676px; height: 115px; display: flex; }
  .tab {
    flex: 1; display: flex; align-items: center; justify-content: center;
    color: var(--white); font-size: 35px; font-weight: 700;
  }
  .tab.new { background: var(--green); }
  .tab.all { background: var(--green-dark); }
</style>
</head>
<body>
<div class="screen">

  <div class="status-bar">
    <div class="carrier">
      <svg width="76" height="14" viewBox="0 0 76 14"><g fill="#fff"><circle cx="7" cy="7" r="6"/><circle cx="22" cy="7" r="6"/><circle cx="37" cy="7" r="6"/></g><g fill="none" stroke="#fff" stroke-width="1.5"><circle cx="52" cy="7" r="5.3"/><circle cx="67" cy="7" r="5.3"/></g></svg>
      <span>NOVA</span>
      <svg width="24" height="18" viewBox="0 0 24 18"><path d="M12 17 2 6a14 14 0 0 1 20 0Z" fill="#fff"/></svg>
    </div>
    <div class="time">4:21 PM</div>
    <div class="battery">
      <svg width="14" height="22" viewBox="0 0 14 22"><path d="M2 6 12 16 7 21V1l5 5L2 16" fill="none" stroke="#fff" stroke-width="1.6"/></svg>
      <span>22%</span>
      <svg width="46" height="22" viewBox="0 0 46 22"><rect x="1" y="2" width="40" height="18" rx="3" fill="none" stroke="#fff" stroke-width="1.6"/><rect x="4" y="5" width="8" height="12" fill="#fff"/><rect x="42" y="8" width="3" height="6" fill="#fff"/></svg>
    </div>
  </div>

  <header class="app-header">
    <svg class="back" width="36" height="54" viewBox="0 0 36 54"><path d="M31 4 7 27l24 23" fill="none" stroke="var(--green)" stroke-width="7" stroke-linecap="round" stroke-linejoin="round"/></svg>
    <div class="brand">prizewell</div>
    <svg class="menu" width="58" height="54" viewBox="0 0 58 54"><g fill="var(--green)"><rect width="58" height="11" rx="5.5"/><rect y="21" width="58" height="11" rx="5.5"/><rect y="42" width="58" height="11" rx="5.5"/></g></svg>
  </header>

  <div class="search-band">
    <div class="search-field">
      <span class="placeholder">Type your text here......</span>
      <svg width="42" height="42" viewBox="0 0 42 42"><circle cx="17" cy="17" r="13" fill="none" stroke="var(--green)" stroke-width="3.5"/><path d="M27 27 38 38" stroke="var(--green)" stroke-width="4.5" stroke-linecap="round"/><path d="M10 15a8 8 0 0 1 6-6" fill="none" stroke="var(--green)" stroke-width="2.5" stroke-linecap="round"/></svg>
    </div>
  </div>

  <article class="sweepstake" style="top:301px">
    <div class="thumb teal" role="img" aria-label="Illustration: Lautsprecherbox mit Kopfhörerkabel"></div>
    <h2 class="title">Lorem Ipsum</h2>
    <p class="teaser">Contrary to popular belief, Lorem</p>
    <p class="deadline"><span>Bis</span><span>2-12-2014</span></p>
    <div class="actions">
      <svg width="42" height="36" viewBox="0 0 42 36" aria-label="Info"><path d="M21 2 2 18h5v16h10V24h8v10h10V18h5Z" fill="#fff"/></svg>
      <svg width="32" height="36" viewBox="0 0 32 36" aria-label="Like"><path d="M2 15h7v19H2ZM11 16 17 3c4 0 5 3 4 8h8c3 0 3 4 1 5 2 1 2 4 0 5 1 1 1 4-1 5 1 2 0 4-3 4H11Z" fill="#fff"/></svg>
      <svg width="46" height="30" viewBox="0 0 46 30" aria-label="Video"><rect x="1" y="5" width="30" height="20" rx="3" fill="#fff"/><circle cx="10" cy="15" r="4" fill="var(--green)"/><circle cx="22" cy="15" r="4" fill="var(--green)"/><path d="M33 15 45 5v20Z" fill="#fff"/></svg>
    </div>
  </article>

  <article class="sweepstake" style="top:455px">
    <div class="thumb orange" role="img" aria-label="Illustration: Geschenkbox mit Schleife"></div>
    <h2 class="title">Lorem Ipsum</h2>
    <p class="teaser">Contrary to popular belief, Lorem</p>
    <p class="deadline"><span>Bis</span><span>2-12-2014</span></p>
    <svg class="reveal" width="32" height="52" viewBox="0 0 32 52"><path d="M28 4 6 26l22 22" fill="none" stroke="var(--green-soft)" stroke-width="7" stroke-linecap="round" stroke-linejoin="round"/></svg>
  </article>

  <article class="sweepstake" style="top:609px">
    <div class="thumb navy" role="img" aria-label="Illustration: Smartphone"></div>
    <h2 class="title">Lorem Ipsum</h2>
    <p class="teaser">Contrary to popular belief, Lorem</p>
    <p class="deadline"><span>Bis</span><span>2-12-2014</span></p>
    <svg class="reveal" width="32" height="52" viewBox="0 0 32 52"><path d="M28 4 6 26l22 22" fill="none" stroke="var(--green-soft)" stroke-width="7" stroke-linecap="round" stroke-linejoin="round"/></svg>
  </article>

  <article class="sweepstake" style="top:764px">
    <div class="thumb navy" role="img" aria-label="Illustration: Landkarte mit Ortsmarker"></div>
    <h2 class="title">Lorem Ipsum</h2>
    <p class="teaser">Contrary to popular belief, Lorem</p>
    <p class="deadline"><span>Bis</span><span>2-12-2014</span></p>
    <svg class="reveal" width="32" height="52" viewBox="0 0 32 52"><path d="M28 4 6 26l22 22" fill="none" stroke="var(--green-soft)" stroke-width="7" stroke-linecap="round" stroke-linejoin="round"/></svg>
  </article>

  <article class="sweepstake" style="top:918px">
    <div class="thumb orange" role="img" aria-label="Illustration: Siegertreppchen mit Sternen"></div>
    <h2 class="title">Lorem Ipsum</h2>
    <p class="teaser">Contrary to popular belief, Lorem</p>
    <p class="deadline"><span>Bis</span><span>2-12-2014</span></p>
    <svg class="reveal" width="32" height="52" viewBox="0 0 32 52"><path d="M28 4 6 26l22 22" fill="none" stroke="var(--green-soft)" stroke-width="7" stroke-linecap="round" stroke-linejoin="round"/></svg>
  </article>

  <article class="sweepstake" style="top:1072px">
    <div class="thumb orange" role="img" aria-label="Illustration eines weiteren Gewinnspiels"></div>
  </article>

  <nav class="tab-bar">
    <div class="tab new">NEU</div>
    <div class="tab all">ALLE</div>
  </nav>

</div>
</body>
</html>
```